Lorna Tess Tresses Fancy Business Card’s

I want my business cards to be elite, original and very classy. I want the business cards to match the colors of my logo and to match the design posted. I would love the design of the picture I posted

I want the card all white .
The dripping on the top of the card I want it to match the pink color in my logo that’s also posted .
I need my logo on the business card !
I need my Instagram- @lorna.tess.tresses__
And my phone number - 582 907 3365

Target Market(s)

My target market is young woman age 23 to older woman to the age of 65
I want both older and younger women to love my design . I don’t want any cheap looking business cards

Industry/Entity Type

Hair And Beauty

Contact Information for Business Card

Add my logo
Add my Instagram- @lorna.tess.tresses__
My number - 582 907 3365
My website- www.lornatesstresses.example

Font styles to use
Serif
Script

Colors
ffffff
e667a6
e34298

Requirements
Must have
• The business cards must have my logo, my number , my website, and my Instagram!
Nice to have
• Nice to have glitter words that match my logo
• The business cards must look classy and mature
• I want them to be very unique!!
Should not have
• Should not have any colors that doesn’t match my logo ! This is very important! Please

```html
<!DOCTYPE html>
<html lang="en">
<head>
<meta charset="utf-8">
<title>Lorna Tess Tresses – Business Card</title>
<link href="https://fonts.googleapis.com/css2?family=Roboto:wght@400;500&family=Great+Vibes&display=swap" rel="stylesheet">
<style>
  :root {
    --backdrop: #3c3c3c;
    --card: #ffffff;
    --pink: #e34298;
    --pink-soft: #e667a6;
    --silver: #8a8a8a;
    --ink: #555555;
    --ink-dark: #3d3d3d;
  }
  * { box-sizing: border-box; margin: 0; padding: 0; }
  html, body {
    width: 1200px; height: 1200px; overflow: hidden;
    background: var(--backdrop);
  }
  .canvas { position: relative; width: 1200px; height: 1200px; }
  .card {
    position: absolute; left: 220px; width: 760px; height: 434px;
    background: var(--card); border-radius: 22px;
    box-shadow: 0 10px 30px rgba(0,0,0,.35);
  }
  .card--front { top: 140px; }
  .card--back { top: 630px; }

  /* Front */
  .front-logo {
    position: absolute; inset: 0;
    display: flex; flex-direction: column; align-items: center; justify-content: center;
  }
  .brand-name {
    font-family: "Roboto", sans-serif; font-weight: 500;
    color: var(--pink); font-size: 64px; line-height: 1.05;
    text-align: center; letter-spacing: 1px;
  }
  .brand-tag {
    margin-top: 18px;
    width: 14px; height: 14px; border-radius: 50%;
    background: var(--pink);
  }

  /* Back */
  .back-logo {
    position: absolute; left: 50px; top: 0; width: 300px; height: 100%;
    display: flex; align-items: center; justify-content: center;
  }
  .back-logo .brand-name { font-size: 40px; }
  .divider {
    position: absolute; left: 372px; top: 110px; width: 2px; height: 215px;
    background: linear-gradient(to bottom, rgba(227,66,152,0), var(--pink) 30%, var(--pink) 70%, rgba(227,66,152,0));
  }
  .details {
    position: absolute; left: 400px; top: 112px;
    font-family: "Roboto", sans-serif;
  }
  .person-name {
    font-family: "Great Vibes", cursive;
    font-size: 46px; line-height: 1; white-space: nowrap;
  }
  .person-name__first { color: var(--pink); }
  .person-name__last { color: var(--silver); }
  .person-role {
    font-size: 22px; color: var(--ink-dark); margin-top: 2px; margin-bottom: 20px;
  }
  .contact-list { list-style: none; }
  .contact-item {
    display: flex; align-items: center; gap: 10px;
    font-size: 20px; color: var(--ink); margin-bottom: 8px; white-space: nowrap;
  }
  .contact-icon {
    width: 20px; height: 20px; flex: none;
    border-radius: 50%; background: var(--pink);
    display: flex; align-items: center; justify-content: center;
  }
</style>
</head>
<body>
<main class="canvas">

  <section class="card card--front" aria-label="Business card front">
    <div class="front-logo">
      <div class="brand-name">Lorna Tess<br>Tresses</div>
      <span class="brand-tag"></span>
    </div>
  </section>

  <section class="card card--back" aria-label="Business card back">
    <div class="back-logo">
      <div class="brand-name">Lorna Tess<br>Tresses</div>
    </div>
    <div class="divider"></div>
    <div class="details">
      <div class="person-name"><span class="person-name__first">Lorna</span> <span class="person-name__last">Tess</span></div>
      <div class="person-role">Custom Wig Maker</div>
      <ul class="contact-list">
        <li class="contact-item">
          <span class="contact-icon">
            <svg width="12" height="12" viewBox="0 0 24 24"><path fill="#fff" d="M6.6 10.8a15.1 15.1 0 0 0 6.6 6.6l2.2-2.2a1 1 0 0 1 1-.25 11.4 11.4 0 0 0 3.6.57 1 1 0 0 1 1 1V20a1 1 0 0 1-1 1A17 17 0 0 1 3 4a1 1 0 0 1 1-1h3.5a1 1 0 0 1 1 1c0 1.25.2 2.45.57 3.6a1 1 0 0 1-.25 1z"/></svg>
          </span>
          582 907 3365
        </li>
        <li class="contact-item">
          <span class="contact-icon"></span>
          @lorna.tess.tresses__
        </li>
        <li class="contact-item">
          <span class="contact-icon">
            <svg width="14" height="14" viewBox="0 0 24 24" fill="none" stroke="#fff" stroke-width="2"><circle cx="12" cy="12" r="9"/><path d="M3 12h18M12 3c3 3.5 3 14.5 0 18M12 3c-3 3.5-3 14.5 0 18"/></svg>
          </span>
          www.lornatesstresses.example
        </li>
      </ul>
    </div>
  </section>

</main>
</body>
</html>
```